The first and only organic certified snacks manufacturer in Singapore (Brightmeadow Foods)needs a pac

We are a Singapore based certified organic snacks manufacturer and raw foods importing company. We deal with a variety of organic products and have been in the Singapore’s food industry for some time now. We are looking for a new packaging design for our product line TALORAN- Plain.
Design requirements:
1.We want a 10x10 cm label design that can be printed at the front and back of a stand-up pouch.
2. We need a design for around 15 different products that are uniform and can be extended easily to cover 30-40 products in future.
3. The stand-up pouch that we will be using is transparent, two sizes (12 x 6 x 21 cm and 16 x 8 x 23 cm), and the label is 10x10 cm
4. We don't have a brand logo and are currently using the word Taloran as the logo, the font is Glacial Indifference.
5.We need a design that is contemporary, clean and simple and using different colour combinations except green and brown(overused by organic competitors)
6.One label/print on each front and back, ca 10x10 cm.
Essential information:
Contents:
1.Filling weight
2.Product nameï‚§
3.Brand name and/or logo (yet to be designed)
4.Originï‚§
5.EU/USDA/HALAL logosï‚§
6.BMF (brightmeadow foods) logo
7.Expiration date

7.The original file should be in the .ai (Adobe Illustrator) format.
Please find attached the certification logos, fonts and the current TALORAN-Plain .ai files

Target Market(s)

everyone who likes to eat and use healthy products

Industry/Entity Type

Food Production

Font styles to use
Other font styles liked:
• Glacial Indiffrence

Colors
fbf063
00a990
85cae6
3377b5
876aae
b768aa
e667a6
f04a50
ffc214

Requirements
Must have
• contemporary clean designs. use of different patterns is suggested
Nice to have
Should not have
• too much use of green, orange and brown colour. pictures of food products.

```html
<!DOCTYPE html>
<html lang="en">
<head>
<meta charset="utf-8">
<title>TALORAN Plain – Label Range</title>
<link rel="stylesheet" href="https://fonts.googleapis.com/css2?family=Poppins:wght@300;400;600;700&display=swap">
<style>
  :root {
    --page: #ffffff;
    --ink: #111111;
    --apricot-bg: #fdd2a0;
    --apricot-line: #a9586a;
    --hazelnut-bg: #cbe9ea;
    --hazelnut-line: #6fc9cc;
    --mulberry-bg: #f9c4b1;
    --mulberry-line: #8c86d1;
    --fig-bg: #fde3a6;
    --fig-line: #f6a889;
  }
  * { margin: 0; padding: 0; box-sizing: border-box; }
  html, body {
    width: 1200px;
    height: 1189px;
    overflow: hidden;
    background: var(--page);
  }
  .label-sheet {
    position: relative;
    width: 1200px;
    height: 1189px;
  }
  .label {
    position: absolute;
    width: 525px;
    height: 526px;
  }
  .label--apricots  { left: 44px;  top: 44px; }
  .label--hazelnuts { left: 624px; top: 44px; }
  .label--mulberries{ left: 44px;  top: 620px; }
  .label--figs      { left: 624px; top: 620px; }

  .label__pattern {
    position: absolute;
    inset: 0;
  }
  .label--apricots .label__pattern {
    background: linear-gradient(135deg, var(--apricot-bg) 0%, #f6c49a 50%, var(--apricot-bg) 100%);
  }
  .label--hazelnuts .label__pattern {
    background: linear-gradient(135deg, var(--hazelnut-bg) 0%, #b3e0e2 50%, var(--hazelnut-bg) 100%);
  }
  .label--mulberries .label__pattern {
    background: linear-gradient(135deg, var(--mulberry-bg) 0%, #efbab9 50%, var(--mulberry-bg) 100%);
  }
  .label--figs .label__pattern {
    background: linear-gradient(135deg, var(--fig-bg) 0%, #fcd39f 50%, var(--fig-bg) 100%);
  }

  .label__panel {
    position: absolute;
    left: 72px;
    top: 81px;
    width: 378px;
    height: 364px;
    background: #ffffff;
    border: 6px solid var(--ink);
  }
  .brand-name {
    position: absolute;
    left: 38px;
    top: 42px;
    font-family: "Poppins", sans-serif;
    font-weight: 700;
    font-size: 37px;
    line-height: 43px;
    letter-spacing: 0.5px;
    color: var(--ink);
  }
  .product-rule {
    position: absolute;
    left: 38px;
    width: 292px;
    height: 2px;
    background: var(--ink);
  }
  .product-rule--top { top: 149px; }
  .product-rule--bottom { top: 251px; }
  .product-process {
    position: absolute;
    left: 38px;
    top: 166px;
    font-family: "Poppins", sans-serif;
    font-weight: 300;
    font-size: 26px;
    line-height: 30px;
    color: var(--ink);
  }
  .product-name {
    position: absolute;
    left: 38px;
    top: 197px;
    font-family: "Poppins", sans-serif;
    font-weight: 300;
    font-size: 38px;
    line-height: 44px;
    color: var(--ink);
  }
  .label__footer {
    position: absolute;
    left: 38px;
    right: 38px;
    top: 296px;
    height: 26px;
    display: flex;
    align-items: center;
  }
  .cert-badges {
    display: flex;
    gap: 6px;
  }
  .cert-badge {
    width: 21px;
    height: 21px;
    border-radius: 50%;
    border: 2px solid var(--ink);
  }
  .maker-mark {
    margin-left: 8px;
    font-family: "Poppins", sans-serif;
    font-weight: 600;
    font-size: 11px;
    color: var(--ink);
    white-space: nowrap;
  }
  .net-weight {
    margin-left: auto;
    font-family: "Poppins", sans-serif;
    font-weight: 400;
    font-size: 11px;
    color: var(--ink);
    white-space: nowrap;
  }
</style>
</head>
<body>
<main class="label-sheet">

  <article class="label label--apricots">
    <div class="label__pattern" role="img" aria-label="Wavy vertical line pattern in maroon on apricot"></div>
    <div class="label__panel">
      <h2 class="brand-name">TALORAN<br>PLAIN</h2>
      <div class="product-rule product-rule--top"></div>
      <p class="product-process">ORGANIC SUN-DRIED</p>
      <p class="product-name">APRICOTS</p>
      <div class="product-rule product-rule--bottom"></div>
      <div class="label__footer">
        <div class="cert-badges"><span class="cert-badge"></span><span class="cert-badge"></span><span class="cert-badge"></span><span class="cert-badge"></span></div>
        <span class="maker-mark">Brightmeadow Foods</span>
        <span class="net-weight">250 G ℮</span>
      </div>
    </div>
  </article>

  <article class="label label--hazelnuts">
    <div class="label__pattern" role="img" aria-label="Wavy vertical line pattern in turquoise on pale aqua"></div>
    <div class="label__panel">
      <h2 class="brand-name">TALORAN<br>PLAIN</h2>
      <div class="product-rule product-rule--top"></div>
      <p class="product-process">ORGANIC ROASTED</p>
      <p class="product-name">HAZELNUTS</p>
      <div class="product-rule product-rule--bottom"></div>
      <div class="label__footer">
        <div class="cert-badges"><span class="cert-badge"></span><span class="cert-badge"></span><span class="cert-badge"></span><span class="cert-badge"></span></div>
        <span class="maker-mark">Brightmeadow Foods</span>
        <span class="net-weight">250 G ℮</span>
      </div>
    </div>
  </article>

  <article class="label label--mulberries">
    <div class="label__pattern" role="img" aria-label="Wavy vertical line pattern in periwinkle on soft pink"></div>
    <div class="label__panel">
      <h2 class="brand-name">TALORAN<br>PLAIN</h2>
      <div class="product-rule product-rule--top"></div>
      <p class="product-process">ORGANIC SUN-DRIED</p>
      <p class="product-name">MULLBERRIES</p>
      <div class="product-rule product-rule--bottom"></div>
      <div class="label__footer">
        <div class="cert-badges"><span class="cert-badge"></span><span class="cert-badge"></span><span class="cert-badge"></span><span class="cert-badge"></span></div>
        <span class="maker-mark">Brightmeadow Foods</span>
        <span class="net-weight">250 G ℮</span>
      </div>
    </div>
  </article>

  <article class="label label--figs">
    <div class="label__pattern" role="img" aria-label="Wavy vertical line pattern in coral on pale yellow"></div>
    <div class="label__panel">
      <h2 class="brand-name">TALORAN<br>PLAIN</h2>
      <div class="product-rule product-rule--top"></div>
      <p class="product-process">ORGANIC SUN-DRIED</p>
      <p class="product-name">FIGS</p>
      <div class="product-rule product-rule--bottom"></div>
      <div class="label__footer">
        <div class="cert-badges"><span class="cert-badge"></span><span class="cert-badge"></span><span class="cert-badge"></span><span class="cert-badge"></span></div>
        <span class="maker-mark">Brightmeadow Foods</span>
        <span class="net-weight">250 G ℮</span>
      </div>
    </div>
  </article>

</main>
</body>
</html>
```